KORBALT

The business want a professional looking business card. We have a scetch we will add but want the extra upgrade, and would like more suggestions for variations of our business cards.

```html
<!DOCTYPE html>
<html lang="en">
<head>
<meta charset="utf-8">
<title>KORBALT — Business Card</title>
<link href="https://fonts.googleapis.com/css2?family=Cinzel:wght@400;500&family=Outfit:wght@300;400;500&display=swap" rel="stylesheet">
<style>
  :root {
    --page-bg: #ffffff;
    --front-light: #c4a868;
    --front-dark: #58401f;
    --back-light: #ede8df;
    --back-mid: #c7ac6a;
    --back-dark: #795a2b;
    --wordmark-gold: #f3dc9c;
    --tagline-cream: #f1e4c4;
    --ink-brown: #6a4a1f;
    --title-brown: #7a5a2c;
    --rule-cream: #f2e3b6;
    --contact-cream: #f6ecd4;
  }
  * { margin: 0; padding: 0; box-sizing: border-box; }
  html, body {
    width: 1200px;
    height: 1200px;
    overflow: hidden;
    background: var(--page-bg);
  }
  .canvas {
    position: relative;
    width: 1200px;
    height: 1200px;
  }
  .card {
    position: absolute;
    left: 305px;
    width: 591px;
    height: 336px;
  }
  .card-front {
    top: 216px;
    background: linear-gradient(135deg, var(--front-light) 0%, #9a7e48 45%, var(--front-dark) 100%);
  }
  .card-back {
    top: 647px;
    background: linear-gradient(120deg, var(--back-light) 0%, var(--back-mid) 40%, #a8874c 70%, var(--back-dark) 100%);
  }
  .line {
    position: absolute;
    left: 0;
    width: 100%;
    text-align: center;
    transform: translateY(-50%);
    white-space: nowrap;
  }
  .brand-name {
    top: 213px;
    font-family: "Cinzel", serif;
    font-weight: 400;
    font-size: 64px;
    letter-spacing: 1px;
    color: var(--wordmark-gold);
  }
  .brand-dot {
    position: absolute;
    left: 50%;
    top: 98px;
    width: 18px;
    height: 18px;
    margin: -9px 0 0 -9px;
    border-radius: 50%;
    background: var(--wordmark-gold);
  }
  .tagline {
    top: 276px;
    font-family: "Outfit", sans-serif;
    font-weight: 400;
    font-size: 17px;
    letter-spacing: 2.5px;
    color: var(--tagline-cream);
  }
  .company-line {
    top: 62px;
    font-family: "Cinzel", serif;
    font-weight: 400;
    font-size: 26px;
    letter-spacing: 1px;
    color: var(--ink-brown);
  }
  .person-name {
    top: 127px;
    font-family: "Outfit", sans-serif;
    font-weight: 500;
    font-size: 23px;
    color: var(--ink-brown);
  }
  .person-title {
    top: 161px;
    font-family: "Outfit", sans-serif;
    font-weight: 400;
    font-size: 17px;
    letter-spacing: 0.3px;
    color: var(--title-brown);
  }
  .divider {
    position: absolute;
    left: 83px;
    top: 192px;
    width: 425px;
    height: 1px;
    background: var(--rule-cream);
  }
  .contact {
    font-family: "Outfit", sans-serif;
    font-weight: 300;
    font-size: 18px;
    color: var(--contact-cream);
  }
  .contact-phone { top: 229px; }
  .contact-email { top: 254px; }
  .contact-web { top: 280px; }
</style>
</head>
<body>
  <main class="canvas">
    <section class="card card-front" aria-label="Card front">
      <span class="brand-dot" aria-hidden="true"></span>
      <h1 class="line brand-name">KORBALT</h1>
      <p class="line tagline">SINCE 2026</p>
    </section>

    <section class="card card-back" aria-label="Card back">
      <p class="line company-line">KORBALT SOLVANG</p>
      <h2 class="line person-name">Lars Henrik Solvang</h2>
      <p class="line person-title">CEO &amp; FOUNDER</p>
      <span class="divider" aria-hidden="true"></span>
      <p class="line contact contact-phone">004791234567</p>
      <p class="line contact contact-email">korbalt.llc@korbaltmail.com</p>
      <p class="line contact contact-web">www.korbalt.llc</p>
    </section>
  </main>
</body>
</html>
```